Web Design Project

To develop a web based Council Meeting Support system which includes 2 major components for each Council member:
1. Allow a council member to Vote on a motion during a council session
2. Allow a council member to flag notify the Chair their intention to speak on a motion
The application will have 3 separate interfaces:
Chair interface: Allows the Chair of the session to review voting and manage the speaker queue
Council interface: Allows each council member to vote on each motion and add flag their intention to speak for or against a motion
Admin interface: Allows administrators to initiate a session and import details on all meeting participants
We will begin by designing the Council Interface. (An example wireframe is attached) This council interface will give members the ability to request to speak, vote, view voting results and viewing the current motion number.
*** 4 Designs will be required overall. One for each interface and a login page ***
Needs to be designed so that it works well on an Velbo or any tablet device.
Update: Looking for a brighter design, not a dark grey one. The blue colour from trm.on.ca would be good.
Flag
- Request to Speak
Voting
Vote Results
Current Motion Number

```html
<!DOCTYPE html>
<html lang="en">
<head>
<meta charset="utf-8">
<title>Council Session – Chair</title>
<link href="https://fonts.googleapis.com/css2?family=Arimo:wght@400;700&family=Tinos:ital,wght@1,700&display=swap" rel="stylesheet">
<style>
:root{
  --brand:#2f6fc4;
  --band:#3b9ec6;
  --band-dark:#2c86ad;
  --navy:#0b2a55;
  --ink:#333;
  --muted:#666;
  --rule:#e2e2e2;
  --for:#e0fddc;
  --against:#fedddd;
  --abstain:#f6f1f1;
  --bar:#d4d4d4;
  --btn-bg:#f0f0f0;
}
*{box-sizing:border-box;margin:0;padding:0}
html,body{width:1084px;height:1200px;overflow:hidden;background:#fff}
body{position:relative;font-family:"Arimo",Arial,sans-serif;color:var(--ink)}
.abs{position:absolute}

.brand{left:133px;top:26px;display:flex;align-items:center;gap:8px}
.brand-mark{width:28px;height:28px;background:var(--brand)}
.brand-name{font-size:20px;font-weight:700;color:var(--brand)}
.nav{right:130px;top:36px;display:flex;gap:32px;font-size:12px;font-weight:700;color:#222}
.nav span::after{content:" »";font-size:9px;color:#999;font-weight:400}
.header-rule{left:0;top:88px;width:1084px;border-top:1px solid var(--rule)}

.motion-band{left:0;top:93px;width:1084px;height:94px;
  background:linear-gradient(180deg,#3fa7d0 0%,var(--band) 55%,var(--band-dark) 100%);color:#fff}
.motion-title{left:130px;top:26px;font-size:19px;font-weight:700}
.motion-desc{left:130px;top:52px;font-size:13px}
.open-label{left:681px;top:26px;font-size:19px;font-weight:700}
.open-list{left:828px;top:24px;display:flex;gap:8px}
.open-list span{width:17px;height:25px;background:var(--navy);color:#fff;
  font-weight:700;font-size:14px;display:flex;align-items:center;justify-content:center}
.band-rule{left:0;top:191px;width:1084px;border-top:1px solid var(--rule)}

.section-title{left:131px;font-size:14px;font-weight:700;color:#222}
.section-rule{left:130px;width:824px;border-top:1px solid var(--rule)}

.controls{left:130px;width:156px;
  background:linear-gradient(90deg,#fff 0%,#f3f3f3 100%);border-right:1px solid #e6e6e6}
.btn-frame{position:absolute;left:27px;width:96px;height:36px;background:#ececec;padding:6px}
.btn{width:84px;height:24px;background:linear-gradient(#fff,#eee);border:1px solid #cfcfcf;
  font-family:"Tinos",Georgia,serif;font-style:italic;font-weight:700;font-size:11px;color:#111;
  display:flex;align-items:center;justify-content:center}

.column{position:absolute;width:217px}
.column svg{position:absolute;left:0;top:0;width:100%;height:100%}
.col-head{position:absolute;left:31px;top:8px;font-size:13px;font-weight:700;color:#333;display:flex;align-items:center;gap:8px}
.col-head i{display:block;width:128px;height:4px;background:var(--bar)}
.col-list{position:absolute;left:31px;top:42px;list-style:none;font-size:12px;color:#555}
.col-list li{height:19.7px;line-height:19.7px}
.col-list li::before{content:"»";font-size:9px;color:#888;display:inline-block;width:17px}
.tally{position:absolute;font-size:11px;font-weight:700;color:#444;transform:translateX(-50%)}

.chair-vote{left:297px;top:1037px;width:639px;height:60px;border:2px solid #ddd;display:flex;align-items:center}
.chair-label{margin-left:20px;font-size:17px;font-weight:700;color:#444;width:115px}
.chair-btn{width:155px;height:21px;background:var(--btn-bg);font-size:10.5px;font-weight:700;
  color:#333;display:flex;align-items:center;justify-content:center;margin-right:8px}

.footer-rule{left:0;top:1139px;width:1084px;border-top:1px solid var(--rule)}
.footer{left:130px;top:1158px;font-size:9.5px;color:#445}
.to-top{right:130px;top:1158px;font-size:9.5px;color:#445}
</style>
</head>
<body>

<header>
  <div class="abs brand"><span class="brand-mark"></span><span class="brand-name">Trillium Registry Council</span></div>
  <nav class="abs nav"><span>Home</span><span>Help</span><span>Logout</span></nav>
  <div class="abs header-rule"></div>
</header>

<section class="abs motion-band">
  <div class="abs motion-title">Current Motion # : 9</div>
  <div class="abs motion-desc">Write any description about current motion.</div>
  <div class="abs open-label">Open Motions :</div>
  <div class="abs open-list"><span>8</span><span>6</span><span>5</span><span>3</span></div>
</section>
<div class="abs band-rule"></div>

<!-- Speaker queue -->
<h2 class="abs section-title" style="top:211px">Speaker Queue:</h2>
<div class="abs section-rule" style="top:237px"></div>

<div class="abs controls" style="top:287px;height:309px">
  <div class="btn-frame" style="top:21px"><div class="btn">Open</div></div>
  <div class="btn-frame" style="top:69px"><div class="btn">Close</div></div>
  <div class="btn-frame" style="top:117px"><div class="btn">Pass</div></div>
  <div class="btn-frame" style="top:165px"><div class="btn">Return</div></div>
</div>

<div class="column" style="left:295px;top:285px;height:232px">
  <svg viewBox="0 0 217 232" preserveAspectRatio="none"><polygon points="0,0 217,0 217,208 108,232 0,208" fill="var(--for)"/></svg>
  <div class="col-head">For <i></i></div>
  <ul class="col-list"><li>A. Adams</li><li>D. Chatia</li><li>L. Chong</li><li>SA. Cupta</li><li>P. Bergeron</li><li>B. Adams</li><li>R. Chui</li><li>S. Cony</li></ul>
</div>
<div class="column" style="left:512px;top:285px;height:193px">
  <svg viewBox="0 0 217 193" preserveAspectRatio="none"><polygon points="0,0 217,0 217,170 108,193 0,170" fill="var(--against)"/></svg>
  <div class="col-head">Against <i style="width:103px"></i></div>
  <ul class="col-list"><li>P. Bergeron</li><li>B. Adams</li><li>R. Chui</li><li>S. Cony</li><li>A. Adams</li><li>D. Chatia</li></ul>
</div>

<!-- Voting -->
<h2 class="abs section-title" style="top:619px">Voting:</h2>
<div class="abs section-rule" style="top:645px"></div>

<div class="abs controls" style="top:699px;height:309px">
  <div class="btn-frame" style="top:17px"><div class="btn">Open</div></div>
  <div class="btn-frame" style="top:65px"><div class="btn">Record Vote</div></div>
</div>

<div class="column" style="left:295px;top:693px;height:234px">
  <svg viewBox="0 0 217 234" preserveAspectRatio="none"><polygon points="0,0 217,0 217,208 108,234 0,208" fill="var(--for)"/></svg>
  <div class="col-head">For <i></i></div>
  <ul class="col-list"><li>A. Adams</li><li>D. Chatia</li><li>L. Chong</li><li>SA. Cupta</li><li>P. Bergeron</li><li>B. Adams</li><li>R. Chui</li><li>S. Cony</li></ul>
</div>
<div class="tally" style="left:403px;top:933px">8 Votes (75%)</div>

<div class="column" style="left:512px;top:693px;height:193px">
  <svg viewBox="0 0 217 193" preserveAspectRatio="none"><polygon points="0,0 217,0 217,169 108,193 0,169" fill="var(--against)"/></svg>
  <div class="col-head">Against <i style="width:103px"></i></div>
  <ul class="col-list"><li>P. Bergeron</li><li>B. Adams</li><li>R. Chui</li><li>S. Cony</li><li>A. Adams</li><li>D. Chatia</li></ul>
</div>
<div class="tally" style="left:620px;top:894px">5 Votes (45%)</div>

<div class="column" style="left:728px;top:693px;height:155px">
  <svg viewBox="0 0 216 155" preserveAspectRatio="none"><polygon points="0,0 216,0 216,131 108,155 0,131" fill="var(--abstain)"/></svg>
  <div class="col-head">Abstain <i style="width:103px"></i></div>
  <ul class="col-list"><li>S. Cony</li><li>A. Adams</li><li>D. Chatia</li><li>L. Chong</li></ul>
</div>
<div class="tally" style="left:837px;top:855px">3 Members</div>

<div class="abs chair-vote">
  <div class="chair-label">Chair Vote:</div>
  <div class="chair-btn">For</div>
  <div class="chair-btn">Against</div>
  <div class="chair-btn">Abstain</div>
</div>

<footer>
  <div class="abs footer-rule"></div>
  <div class="abs footer">Copyright 2012 Trillium Registry Council &nbsp;|&nbsp; All Rights Reserved &nbsp;|&nbsp; webmaster</div>
  <div class="abs to-top">Back to the top »</div>
</footer>

</body>
</html>
```